web design for specialty coffee shop

We are online shop selling specialty coffeee.
Our brand concept keywords are -
specialty coffee, knowledge, discovery, professional, convenience, collaboration.
there will be five main tabs on the homepage
[home (u icon from logo)]
[coffee]
[equipment]
[gift]
[knowledge]
[about us]
For our site, we will be using the following template.
ONLY DESIGN, NO CODING necessary as our developers will do that.
http://layoutbarn.example/item/velorina-deluxe-adaptive-storefront-theme/full_screen_preview/7351620
Use the template as a base.
You do not have to do exactly the same layout.
Creative Liberty!
For the style and color palette, please look at the attached image.
Our brown logo should match nicely with the style provided in the attachment.
Thank you for taking the time to read this post.
Looking forward to working with artmingle and the amazing designers that are part of this community.
Reason: Dear designers,
I have extended the deadline to give designers who accepted to participate in this contest some more time to submit their designs. Thank you for understanding.

```html
<!DOCTYPE html>
<html lang="en">
<head>
<meta charset="utf-8">
<title>Kestrel Coffee Lab</title>
<link rel="stylesheet" href="https://fonts.googleapis.com/css2?family=Didact+Gothic&family=Carlito:ital,wght@0,400;0,700;1,400&family=Lato:wght@900&display=swap">
<style>
:root{
  --parchment-light:#e9dcb4;
  --parchment-mid:#d2bd86;
  --parchment-dark:#a98d52;
  --espresso:#2a1f1b;
  --roast:#3b2a22;
  --mocha:#6d4a33;
  --body-brown:#6b4a35;
  --mist:#f2f5f4;
  --white:#ffffff;
  --field-line:#c9c9c9;
  --arrow-grey:#8c8480;
}
*{box-sizing:border-box;margin:0;padding:0}
html,body{width:1120px;height:1200px;overflow:hidden;background:var(--mist)}
body{position:relative;font-family:"Carlito",sans-serif;color:var(--espresso)}
.parchment{
  background:
    radial-gradient(ellipse at 20% 40%,rgba(255,250,225,.55),transparent 60%),
    radial-gradient(ellipse at 75% 60%,rgba(255,245,210,.45),transparent 55%),
    linear-gradient(180deg,var(--parchment-dark) 0%,var(--parchment-mid) 18%,var(--parchment-light) 50%,var(--parchment-mid) 82%,var(--parchment-dark) 100%);
}
.site-header{position:absolute;left:0;top:0;width:1120px;height:160px;z-index:3;box-shadow:0 4px 6px rgba(42,31,27,.7)}
.brand{position:absolute;left:90px;top:26px;width:142px;height:142px;border-radius:50%;
  background:var(--parchment-mid);border:2px solid var(--roast);display:flex;align-items:center;justify-content:center;text-align:center}
.brand-name{font-family:"Didact Gothic",sans-serif;font-size:19px;line-height:1.15;color:var(--roast)}
.account{position:absolute;right:82px;top:30px;text-align:right;font-family:"Didact Gothic",sans-serif;font-size:21px;line-height:27px;color:var(--espresso)}
.main-nav{position:absolute;right:82px;top:114px;font-family:"Didact Gothic",sans-serif;font-size:28px;color:var(--espresso);white-space:nowrap}
.hero{position:absolute;left:80px;top:168px;width:960px;height:472px;z-index:1;
  background:
    radial-gradient(ellipse 300px 230px at 330px 110px,rgba(252,251,249,1) 0%,rgba(245,240,232,.9) 45%,rgba(245,240,232,0) 100%),
    radial-gradient(ellipse 260px 200px at 800px 150px,rgba(246,244,240,.9) 0%,rgba(246,244,240,0) 100%),
    radial-gradient(ellipse at 40% 85%,#6b4126 0%,#7e5232 40%,rgba(126,82,50,0) 85%),
    linear-gradient(180deg,#efe9e1 0%,#b48a62 45%,#8a5c38 75%,#a87a52 100%)}
.slide-arrow{position:absolute;top:370px}
.slide-arrow.prev{left:18px}
.slide-arrow.next{left:1050px}
.store-finder{position:absolute;left:684px;top:226px;width:316px;height:294px;z-index:2;background:rgba(255,255,255,.82)}
.store-finder h2{position:absolute;left:38px;top:42px;font-family:"Didact Gothic",sans-serif;font-weight:700;font-size:21px;color:var(--roast);-webkit-text-stroke:.4px var(--roast)}
.finder-row{position:absolute;left:0;width:316px;height:25px}
.finder-row label{position:absolute;right:188px;top:2px;font-family:"Didact Gothic",sans-serif;font-size:16px;color:var(--roast)}
.finder-row .select{position:absolute;left:137px;top:0;width:130px;height:24px;border:1px solid var(--field-line);background:var(--white)}
.finder-row .select svg{position:absolute;right:0;top:0}
.finder-submit{position:absolute;left:165px;top:208px;width:77px;height:30px;background:var(--espresso);color:var(--white);
  font-family:"Didact Gothic",sans-serif;font-size:14px;line-height:30px;text-align:center;box-shadow:2px 2px 4px rgba(0,0,0,.4)}
.hero-shadow{position:absolute;left:200px;top:644px;width:720px;height:60px;border-radius:50%;background:radial-gradient(ellipse,var(--roast) 55%,rgba(59,42,34,0) 72%)}
.about{position:absolute;left:80px;top:712px;width:956px}
.about h1{font-family:"Didact Gothic",sans-serif;font-weight:400;font-size:30px;line-height:36px;color:var(--espresso)}
.about-line{display:block;font-size:25px;line-height:33.5px;color:var(--body-brown);white-space:nowrap;text-align:justify;text-align-last:justify}
.about-line.first{margin-top:-4px;padding-left:160px}
.about-line.last{text-align-last:left}
.read-more{position:absolute;right:0;top:188px;font-family:"Didact Gothic",sans-serif;font-size:28px;color:var(--espresso)}
.site-footer{position:absolute;left:0;top:960px;width:1120px;height:240px}
.footer-title{position:absolute;top:24px;font-family:"Lato",sans-serif;font-weight:900;font-size:20px;letter-spacing:.4px;color:var(--roast)}
.testimonial{position:absolute;left:80px;top:58px;width:304px;height:112px;background:var(--white);border-radius:3px}
.testimonial .avatar{position:absolute;left:10px;top:10px;width:84px;height:92px;border-radius:50%;background:linear-gradient(160deg,#5b4a42,#c79a80 60%,#2c2420)}
.testimonial p{position:absolute;left:112px;top:16px;font-size:16px;line-height:21px;color:var(--espresso)}
.testimonial cite{display:block;margin-left:7px;margin-top:3px;font-style:normal}
.testimonial cite em{font-style:italic}
.email-field{position:absolute;left:453px;top:60px;width:267px;height:26px;background:var(--white);font-style:italic;font-size:16px;line-height:26px;padding-left:21px;color:var(--espresso)}
.subscribe-btn{position:absolute;left:530px;top:94px;width:108px;height:28px;background:var(--white);text-align:center;font-size:16px;line-height:28px;color:var(--espresso)}
.social{position:absolute;left:514px;top:144px;display:flex;gap:12px}
.social span{width:26px;height:26px;border:1px solid var(--arrow-grey);border-radius:3px;background:#eee;display:flex;align-items:center;justify-content:center}
.social span::after{content:"";width:14px;height:14px;background:var(--espresso);border-radius:2px}
.address{position:absolute;left:788px;top:52px;font-size:19px;line-height:24px;color:var(--espresso);font-style:normal}
.copyright{position:absolute;left:0;width:1120px;top:206px;text-align:center;font-family:"Didact Gothic",sans-serif;font-size:15px;color:var(--espresso)}
.copyright span{margin:0 14px}
</style>
</head>
<body>
<header class="site-header parchment">
  <div class="brand"><span class="brand-name">Kestrel<br>Coffee Lab</span></div>
  <div class="account">Login / Register<br>Call: (1800)-555-0142</div>
  <nav class="main-nav">Coffee / Equipment / Gift / Knowledge / About Us</nav>
</header>

<section class="hero" role="img" aria-label="Photo of a white coffee cup with a clock-shaped crema pattern on a saucer, surrounded by roasted coffee beans"></section>

<svg class="slide-arrow prev" width="52" height="60" viewBox="0 0 52 60" aria-hidden="true"><polygon points="4,30 48,4 48,56" fill="none" stroke="var(--roast)" stroke-width="9"/></svg>
<svg class="slide-arrow next" width="52" height="60" viewBox="0 0 52 60" aria-hidden="true"><polygon points="48,30 4,4 4,56" fill="none" stroke="var(--roast)" stroke-width="9"/></svg>

<form class="store-finder">
  <h2>Locate a Store</h2>
  <div class="finder-row" style="top:78px"><label>Select zone</label><div class="select"><svg width="22" height="22"><line x1="0" y1="0" x2="0" y2="22" stroke="#ccc"/><polygon points="5,6 17,6 11,16" fill="var(--arrow-grey)"/></svg></div></div>
  <div class="finder-row" style="top:109px"><label>State</label><div class="select"><svg width="22" height="22"><line x1="0" y1="0" x2="0" y2="22" stroke="#ccc"/><polygon points="5,6 17,6 11,16" fill="var(--arrow-grey)"/></svg></div></div>
  <div class="finder-row" style="top:140px"><label>City</label><div class="select"><svg width="22" height="22"><line x1="0" y1="0" x2="0" y2="22" stroke="#ccc"/><polygon points="5,6 17,6 11,16" fill="var(--arrow-grey)"/></svg></div></div>
  <div class="finder-row" style="top:170px"><label>Area</label><div class="select"><svg width="22" height="22"><line x1="0" y1="0" x2="0" y2="22" stroke="#ccc"/><polygon points="5,6 17,6 11,16" fill="var(--arrow-grey)"/></svg></div></div>
  <div class="finder-submit">Submit</div>
</form>

<div class="hero-shadow"></div>

<section class="about">
  <h1>About Us</h1>
  <p>
    <span class="about-line first">Lorem ipsum dolor sit amet, consectetuer adipiscing elit. Aenean com-</span>
    <span class="about-line">modo ligula eget dolor. Aenean massa. Cum sociis natoque penatibus et magnis dis</span>
    <span class="about-line">parturient montes, nascetur ridiculus mus. Donec quam felis, ultricies nec, pellen-</span>
    <span class="about-line">tesque eu, pretium quis, sem. Nulla consequat massa quis enim. Donec pede justo,</span>
    <span class="about-line last">fringilla vel, aliquet nec, vulputate eget, arcu...............</span>
  </p>
  <a class="read-more">Read More &gt;&gt;</a>
</section>

<footer class="site-footer parchment">
  <h3 class="footer-title" style="left:84px">Customer Testimonials</h3>
  <div class="testimonial">
    <div class="avatar" role="img" aria-label="Customer portrait photo"></div>
    <p>Its a really good service<br>and r really very nice<br>delevery time<cite>By- <em>Daniel Reyes</em></cite></p>
  </div>

  <h3 class="footer-title" style="left:456px">Subscribe for Alerts</h3>
  <div class="email-field">Enter Your E-mail id here</div>
  <div class="subscribe-btn">Submit</div>
  <div class="social"><span></span><span></span><span></span><span></span></div>

  <h3 class="footer-title" style="left:824px">Address</h3>
  <address class="address">Kestrel Coffee Lab<br>Maple Court, 18 Ardent Street,<br>Hollow Road,<br>London.<br>Call on: 1822-555-017</address>

  <div class="copyright"><span>Copyright 2013 by HartwellBros</span><span>Powred by QuillStudio</span></div>
</footer>
</body>
</html>
```